Stationary Design for an engineering start-up.

Company name: Lumaret Grain Inc.

Our advanced materials company utilizes a patented process to spray-coat wood surfaces with metal. Metal is sprayed as a super-heated powder and fully conforms to the surface of the wood allowing for a wide range of applications. Metals used are COPPER and BRONZE.

We need a stationary package that includes Business Card, Letter Head, and Envelope.

- After we will submit a contest for a brochure design, so a winning designer will have advantage to take that project as well.

Target Market(s)

Our target market are building and industrial design professionals.

- Architects
- Designers
- Builders

Industry/Entity Type

Engineering

Requirements
Must have
• - All stationary must include our logo (attached)

Sizes:
Business card: Standard 3.5 by 2 inches. Landscape.

Letterhead: 8.5" x 11"

Envelopes:
One standard commercial size #10 (4 1/8" by 9 1/2")
One catalog size envelope (9" by 12")
Assume envelopes are one-sided (front print only)

- Use bleeds where applicable

- Include all fonts used.

File Format:
AI or PSD
** for letterhead please include MSWord template.
Nice to have
• Design style
- Take design style from our logo and attached images.
- Modern, sharp, minimalistic
- Sans fonts
- Don''t be afraid to use color background for business card.
We''re open to ideas of making the business card somehow representative of the product - metal coated wood.

```html
<!DOCTYPE html>
<html lang="en">
<head>
<meta charset="utf-8">
<title>Lumaret Grain Inc. — Stationery Set</title>
<link rel="stylesheet" href="https://fonts.googleapis.com/css2?family=Arimo:wght@400;700&display=swap">
<style>
  :root {
    --board: #8a927a;
    --paper: #fdfdfc;
    --ink: #1d1b18;
    --ink-soft: #3a3630;
    --copper: #b5561a;
    --bronze-text: #6b3a18;
    --gold-light: #efe6bf;
    --gold-mid: #d8c98b;
    --gold-deep: #c2ac5c;
    --rule: #c9c6ba;
    --mark: #c9301c;
  }
  * { margin: 0; padding: 0; box-sizing: border-box; }
  html, body { width: 1200px; height: 1200px; overflow: hidden; }
  body {
    background: var(--board);
    font-family: "Arimo", Arial, sans-serif;
    color: var(--ink);
    position: relative;
  }
  .piece {
    position: absolute;
    overflow: hidden;
    background: var(--paper);
    box-shadow: 3px 4px 6px rgba(0,0,0,0.35);
  }
  .piece .swoosh { position: absolute; inset: 0; width: 100%; height: 100%; }
  .brand { position: absolute; display: flex; flex-direction: column; }
  .brand-row { display: flex; align-items: center; }
  .brand-square { background: var(--mark); flex: none; }
  .brand-name { letter-spacing: 0.08em; color: var(--ink); font-weight: 400; line-height: 1; }
  .brand-tagline { color: var(--ink-soft); }

  /* Letterhead */
  .letterhead { left: 54px; top: 43px; width: 550px; height: 712px; }
  .letterhead .brand { left: 28px; top: 36px; }
  .letterhead .brand-square { width: 26px; height: 26px; margin-right: 8px; }
  .letterhead .brand-name { font-size: 30px; }
  .letterhead .brand-tagline { font-size: 12.5px; margin: 3px 0 0 56px; }
  .letterhead-footer {
    position: absolute; left: 72px; right: 14px; top: 655px;
    border-top: 1px solid var(--rule); padding-top: 8px;
    font-size: 10.5px; color: var(--ink-soft); text-align: center;
  }
  .letterhead-footer .contact-line { display: flex; gap: 20px; padding-left: 6px; }
  .letterhead-footer .web { color: var(--copper); margin-top: 12px; padding-right: 30px; }

  /* Business cards */
  .card { width: 463px; height: 264px; }
  .card-front { left: 636px; top: 43px; background: linear-gradient(100deg, var(--gold-light), var(--gold-mid) 55%, var(--gold-deep)); }
  .card-back {
    left: 638px; top: 339px; width: 457px; height: 262px;
    background: linear-gradient(100deg, var(--gold-light), var(--gold-mid) 55%, var(--gold-deep));
  }
  .brushed {
    position: absolute; inset: 0;
    background: repeating-linear-gradient(90deg, rgba(255,255,255,0.10) 0 2px, rgba(120,100,40,0.06) 2px 5px, rgba(255,255,255,0.04) 5px 9px);
  }
  .card-front .brand { left: 18px; top: 20px; }
  .card-front .brand-square { width: 42px; height: 42px; margin-right: 10px; }
  .card-front .brand-name { font-size: 38px; }
  .card-front .brand-tagline { font-size: 20px; margin: 4px 0 0 64px; }
  .card-phone {
    position: absolute; left: 42px; top: 164px; font-size: 14.5px; line-height: 1.22;
    display: grid; grid-template-columns: 32px auto; color: var(--ink);
  }
  .card-phone dd { color: var(--ink-soft); }
  .card-address { position: absolute; left: 265px; top: 107px; font-size: 14.5px; line-height: 1.22; color: var(--ink-soft); font-style: normal; }
  .card-address strong { color: var(--ink); font-weight: 400; }
  .card-web { position: absolute; left: 265px; top: 222px; font-size: 14.5px; color: var(--ink-soft); }
  .card-back .brand { left: 0; right: 0; top: 56px; align-items: center; }
  .card-back .brand-square { width: 42px; height: 42px; margin-bottom: 20px; }
  .card-back .brand-name { font-size: 40px; letter-spacing: 0.1em; }
  .card-back .web { font-size: 14px; margin-top: 6px; color: var(--ink); }

  /* #10 envelope */
  .envelope-10 { left: 30px; top: 823px; width: 663px; height: 289px; }
  .envelope-10 .brand { left: 40px; top: 24px; }
  .envelope-10 .brand-square { width: 24px; height: 24px; margin-right: 6px; }
  .envelope-10 .brand-name { font-size: 22px; }
  .envelope-10 .brand-tagline { font-size: 10.5px; margin: 2px 0 0 34px; }

  /* Catalog envelope */
  .envelope-catalog { left: 636px; top: 654px; width: 536px; height: 403px; }
  .envelope-catalog .brand { left: 35px; top: 26px; }
  .envelope-catalog .brand-square { width: 26px; height: 26px; margin-right: 6px; }
  .envelope-catalog .brand-name { font-size: 24px; }
  .envelope-catalog .brand-tagline { font-size: 11px; margin: 3px 0 0 38px; }

  .envelope-footer {
    position: absolute; border-top: 1px solid var(--rule); padding-top: 6px;
    font-size: 7px; color: var(--ink-soft); display: flex; justify-content: space-between;
    white-space: nowrap;
  }
  .envelope-footer b { color: var(--bronze-text); }
  .envelope-10 .envelope-footer { left: 160px; right: 30px; top: 265px; padding-left: 12px; padding-right: 8px; }
  .envelope-catalog .envelope-footer { left: 160px; right: 18px; top: 384px; font-size: 6.4px; padding-left: 8px; }
</style>
</head>
<body>
  <svg width="0" height="0" style="position:absolute" aria-hidden="true">
    <defs>
      <linearGradient id="copperFlow" x1="0" y1="0" x2="1" y2="1">
        <stop offset="0" stop-color="#3a1a0a"/>
        <stop offset="0.3" stop-color="#b5561a"/>
        <stop offset="0.55" stop-color="#4a220c"/>
        <stop offset="0.8" stop-color="#c46a28"/>
        <stop offset="1" stop-color="#2e1408"/>
      </linearGradient>
    </defs>
  </svg>

  <!-- Letterhead -->
  <section class="piece letterhead">
    <svg class="swoosh" viewBox="0 0 550 712" preserveAspectRatio="none" role="img" aria-label="Flowing copper and dark wood abstract band">
      <path d="M0 0 H28 Q2 380 80 712 H0 Z" fill="url(#copperFlow)"/>
    </svg>
    <div class="brand">
      <div class="brand-row"><span class="brand-square"></span><span class="brand-name">LUMARET</span></div>
      <span class="brand-tagline">Lumaret Grain Inc.</span>
    </div>
    <footer class="letterhead-footer">
      <div class="contact-line">
        <span>48 Foundry Ln., Brassvale, Northfield, 5K7 2M9</span>
        <span>Tel - 555.014.2281</span>
        <span>Fax - 555.014.2282</span>
      </div>
      <div class="web">www.lumaretgrain.com</div>
    </footer>
  </section>

  <!-- Business card front -->
  <section class="piece card card-front">
    <div class="brushed"></div>
    <svg class="swoosh" viewBox="0 0 463 264" preserveAspectRatio="none" role="img" aria-label="Copper coated wood corners">
      <path d="M0 0 H14 Q10 170 82 264 H0 Z" fill="url(#copperFlow)"/>
      <path d="M395 0 H463 V264 H447 Q470 110 395 0 Z" fill="url(#copperFlow)"/>
    </svg>
    <div class="brand">
      <div class="brand-row"><span class="brand-square"></span><span class="brand-name">LUMARET</span></div>
      <span class="brand-tagline">Lumaret Grain Inc.</span>
    </div>
    <dl class="card-phone">
      <dt>Tel</dt><dd>555.014.2281</dd>
      <dt>Fax</dt><dd>555.014.2282</dd>
    </dl>
    <address class="card-address">
      <strong>Address</strong><br>48 Foundry Ln.<br>Brassvale<br>Northfield<br>5K7 2M9
    </address>
    <div class="card-web">www.lumaretgrain.com</div>
  </section>

  <!-- Business card back -->
  <section class="piece card-back">
    <div class="brushed"></div>
    <div class="brand">
      <span class="brand-square"></span>
      <span class="brand-name">LUMARET</span>
      <span class="web">www.lumaretgrain.com</span>
    </div>
  </section>

  <!-- #10 envelope -->
  <section class="piece envelope-10">
    <svg class="swoosh" viewBox="0 0 663 289" preserveAspectRatio="none" role="img" aria-label="Flowing copper and dark wood abstract corner">
      <path d="M0 0 H42 Q0 160 150 289 H0 Z" fill="url(#copperFlow)"/>
    </svg>
    <div class="brand">
      <div class="brand-row"><span class="brand-square"></span><span class="brand-name">LUMARET</span></div>
      <span class="brand-tagline">Lumaret Grain Inc.</span>
    </div>
    <footer class="envelope-footer">
      <span><b>Address - </b>48 Foundry Ln., Brassvale, Northfield, 5K7 2M9</span>
      <span><b>Tel - </b>555.014.2281</span>
      <span><b>Fax - </b>555.014.2282</span>
      <span>www.lumaretgrain.com</span>
    </footer>
  </section>

  <!-- Catalog envelope -->
  <section class="piece envelope-catalog">
    <svg class="swoosh" viewBox="0 0 536 403" preserveAspectRatio="none" role="img" aria-label="Flowing copper and dark wood abstract corner">
      <path d="M0 0 H24 Q0 260 170 403 H0 Z" fill="url(#copperFlow)"/>
    </svg>
    <div class="brand">
      <div class="brand-row"><span class="brand-square"></span><span class="brand-name">LUMARET</span></div>
      <span class="brand-tagline">Lumaret Grain Inc.</span>
    </div>
    <footer class="envelope-footer">
      <span><b>Address - </b>48 Foundry Ln., Brassvale, Northfield 5K7 2M9</span>
      <span><b>Tel/Fax - </b>555.014.2281</span>
      <span>www.lumaretgrain.com</span>
    </footer>
  </section>
</body>
</html>
```